Webdesign für Projektmanagement
Zielgruppe
Projektmanagement und Projektsteuerung von Bauvorhaben für Projektentwickler und Bauträger.
Wesentliche Bereiche sind Wirtschaftliche Steuerung, Steuerung der Baustelle und Bauabläufe sowie Steuerung der Marketing und Vertriebsaktivitäten.
Aufgabenstellung
Orientierung am Logo. Logo und Visitenkarte liegen bei. Schriftart Prelo und Prelo Slab.

```html
<!DOCTYPE html>
<html lang="de">
<head>
<meta charset="utf-8">
<title>Brandeck Bauwerte – Projektmanagement</title>
<link href="https://fonts.googleapis.com/css2?family=Raleway:ital,wght@0,200;0,300;0,400;0,500;0,600;0,700;1,300;1,400&display=swap" rel="stylesheet">
<style>
  :root{
    --navy:#0b2540;
    --page:#00233e;
    --gold:#9c8446;
    --white:#ffffff;
    --card:#f1f0ee;
    --text:#3b3b3b;
    --muted:#6d6d6d;
    --line:#ececec;
  }
  *{margin:0;padding:0;box-sizing:border-box}
  html,body{width:1036px;height:1200px;overflow:hidden;background:var(--page)}
  body{font-family:"Raleway",sans-serif;position:relative}
  .site{position:absolute;left:18px;top:312px;width:1000px;height:576px;display:flex;box-shadow:0 10px 30px rgba(0,0,0,.35)}
  .sidebar{width:152px;height:100%;background:var(--white);position:relative}
  .brand{position:absolute;left:23px;top:54px;color:var(--navy);font-weight:700;font-size:17px;line-height:1.05;letter-spacing:-.2px}
  .brand small{display:block;font-size:9px;font-weight:700;letter-spacing:.4px;margin-top:2px}
  .nav{position:absolute;top:140px;left:0;right:0;list-style:none;border-top:1px solid var(--line)}
  .nav li{height:30.6px;border-bottom:1px solid var(--line);display:flex;align-items:center;justify-content:space-between;padding:0 16px 0 23px;font-size:9px;font-weight:500;color:var(--navy);letter-spacing:.3px}
  .nav li.active{color:var(--gold);font-weight:700}
  .nav .chev{width:5px;height:8px}
  .nav .search{color:#999;font-style:italic;font-weight:300;justify-content:flex-start;gap:8px}
  .social{position:absolute;top:547px;left:33px;display:flex;gap:9px}
  .social span{width:10px;height:10px;background:var(--navy);border-radius:50%}
  .main{flex:1;position:relative;overflow:hidden}
  .photo{position:absolute;inset:0;background:
    radial-gradient(ellipse at 30% 10%,rgba(230,205,140,.9),rgba(230,205,140,0) 55%),
    radial-gradient(ellipse at 80% 40%,rgba(190,140,90,.55),rgba(190,140,90,0) 45%),
    linear-gradient(180deg,#cfb77e 0%,#d3c6a0 45%,#c8c5b4 75%,#bfbcab 100%)}
  .topbar{position:absolute;left:0;right:0;top:0;height:29px;background:rgba(120,105,70,.45);display:flex;align-items:center;gap:17px;padding-left:53px;color:var(--white);font-size:8.5px;font-weight:300}
  .topbar span{display:flex;align-items:center;gap:5px}
  .topbar svg{width:9px;height:9px}
  .hero{position:absolute;left:53px;top:146px}
  .kicker{font-size:15px;font-weight:700;color:var(--navy);letter-spacing:.3px}
  .headline{margin-top:18px;font-size:47px;font-weight:200;color:var(--white);line-height:56px;letter-spacing:.5px}
  .cards{position:absolute;left:53px;top:341px;display:flex;gap:9px}
  .card{width:200px;height:141px;background:var(--card);position:relative;padding:10px 12px}
  .card .cat{font-size:8.5px;font-style:italic;font-weight:400;color:var(--muted)}
  .card h3{margin-top:8px;font-size:9.6px;font-weight:600;color:var(--gold);line-height:13px}
  .card p{margin-top:7px;font-size:8.5px;font-weight:400;color:var(--text);line-height:13px}
  .card .more{position:absolute;right:0;bottom:0;width:76px;height:20px;background:var(--navy);color:var(--white);font-size:7.5px;font-weight:700;display:flex;align-items:center;justify-content:center;letter-spacing:.3px}
  .footer{position:absolute;left:0;right:0;bottom:0;height:35px;background:rgba(150,145,125,.45);display:flex;align-items:center;padding-left:53px;font-size:8.5px;color:#3d3d3d}
</style>
</head>
<body>
<div class="site">
  <aside class="sidebar">
    <div class="brand">Brandeck<small>Bauwerte</small></div>
    <ul class="nav">
      <li class="active">HOME</li>
      <li>LEISTUNGEN</li>
      <li>ÜBER UNS <svg class="chev" viewBox="0 0 5 8"><path d="M1 1l3 3-3 3" fill="none" stroke="#9c8446"/></svg></li>
      <li>PROJEKTE <svg class="chev" viewBox="0 0 5 8"><path d="M1 1l3 3-3 3" fill="none" stroke="#9c8446"/></svg></li>
      <li>PARTNER</li>
      <li>KONTAKT</li>
      <li class="search"><svg width="7" height="7" viewBox="0 0 8 8"><circle cx="3.2" cy="3.2" r="2.3" fill="none" stroke="#9c8446" stroke-width="1.2"/><path d="M5 5l2.4 2.4" stroke="#9c8446" stroke-width="1.3"/></svg>Suchen</li>
    </ul>
    <div class="social" aria-label="Soziale Netzwerke"><span></span><span></span><span></span><span></span></div>
  </aside>
  <main class="main">
    <div class="photo" role="img" aria-label="Foto: Hand mit Stift über Bauplänen am Schreibtisch, warmes Licht"></div>
    <div class="topbar">
      <span><svg viewBox="0 0 10 10"><path d="M2 1l2 0 1 2-1.2 1a5 5 0 0 0 2.2 2.2L7 5l2 1v2c-4 .5-7.5-3-7-7z" fill="#0b2540"/></svg>+49 (0)000 - 123 456 78</span>
      <span><svg viewBox="0 0 10 10"><circle cx="5" cy="5" r="4" fill="none" stroke="#0b2540" stroke-width="1.1"/><path d="M5 2.5V5h2" fill="none" stroke="#0b2540"/></svg>Mo - Fr 9:00 - 18:00</span>
      <span><svg viewBox="0 0 10 10"><rect x=".5" y="2" width="9" height="6" fill="none" stroke="#0b2540"/><path d="M.5 2l4.5 3.5L9.5 2" fill="none" stroke="#0b2540"/></svg>kontakt@brandeck-bau.de</span>
      <span><svg viewBox="0 0 10 10"><path d="M5 .5a3.2 3.2 0 0 1 3.2 3.2C8.2 6 5 9.5 5 9.5S1.8 6 1.8 3.7A3.2 3.2 0 0 1 5 .5z" fill="#0b2540"/><circle cx="5" cy="3.7" r="1.1" fill="#cdbb8a"/></svg>Lindenhofweg 12, 40000 Musterstadt</span>
    </div>
    <section class="hero">
      <h2 class="kicker">PROJEKTMANAGEMENT &amp; PROJEKTSTEUERUNG</h2>
      <h1 class="headline">WIR REALISIEREN<br>BAUVORHABEN</h1>
    </section>
    <section class="cards">
      <article class="card">
        <div class="cat">Betriebswirtschaftliche Planung</div>
        <h3>STET CLITA KASD GUBERGREN NO SEA TAKIMATA SANCTUS EST LOREM</h3>
        <p>Lorem ipsum dolor sit amet, consetetur sadipscing elitr, sed diam nonumy eirmod tempor invidunt ut labore et dolore magna aliquyam erat, sed diam voluptua.</p>
        <div class="more">WEITERLESEN</div>
      </article>
      <article class="card">
        <div class="cat">Steuerung der baulichen Umsetzung</div>
        <h3>STET CLITA KASD GUBERGREN NO SEA TAKIMATA SANCTUS EST LOREM</h3>
        <p>Lorem ipsum dolor sit amet, consetetur sadipscing elitr, sed diam nonumy eirmod tempor invidunt ut labore et dolore magna aliquyam erat, sed diam voluptua.</p>
        <div class="more">WEITERLESEN</div>
      </article>
      <article class="card">
        <div class="cat">Marketing und Vertrieb</div>
        <h3>STET CLITA KASD GUBERGREN NO SEA TAKIMATA SANCTUS EST LOREM</h3>
        <p>Lorem ipsum dolor sit amet, consetetur sadipscing elitr, sed diam nonumy eirmod tempor invidunt ut labore et dolore magna aliquyam erat, sed diam voluptua.</p>
        <div class="more">WEITERLESEN</div>
      </article>
    </section>
    <footer class="footer">© 2017 Brandeck Bauwerte GmbH - Impressum</footer>
  </main>
</div>
</body>
</html>
```